A5 Personal trainer profile for brackmoor wellness

I need a A5 Landscape profile designed for the company I work for. Company name is Brackmoor Wellness. The profile is for personal trainers to let people know:

1. Brief description of themselves
2. Qualifications

A picture will be required on the right hand side of the profile. Brackmoor Wellness colours are green and white.

The Brackmoor Wellness Logo in the boarder of the example included must remain. We are looking for a clinical and professional design.

Industry/Entity Type

Health

```html
<!DOCTYPE html>
<html lang="en">
<head>
<meta charset="utf-8">
<title>Daniel Okafor – Personal Trainer Profile | Brackmoor Wellness</title>
<link href="https://fonts.googleapis.com/css2?family=Arimo:wght@400;700&family=Tinos:ital,wght@0,700;1,700&display=swap" rel="stylesheet">
<style>
  :root {
    --pale-green: #e3eec4;
    --band-line: #d5e5a8;
    --brand-green: #5ea83a;
    --text-green: #6cae3f;
    --white: #ffffff;
    --photo-top: #d7e6a6;
    --photo-bottom: #b9d27a;
  }
  * { margin: 0; padding: 0; box-sizing: border-box; }
  html, body { width: 1200px; height: 857px; overflow: hidden; background: var(--white); }
  .profile {
    position: relative; width: 1200px; height: 857px;
    background: var(--white);
    font-family: "Arimo", Arial, sans-serif;
    color: var(--text-green);
    overflow: hidden;
  }
  .services {
    position: absolute; left: 0; top: 0; width: 1200px; height: 380px;
    background: var(--pale-green);
  }
  .services__title {
    position: absolute; left: 72px; top: 38px;
    font-family: "Tinos", "Times New Roman", serif;
    font-style: italic; font-weight: 700; font-size: 42px; line-height: 50px;
    color: var(--brand-green);
  }
  .services__list {
    position: absolute; left: 56px; top: 104px;
    list-style: none;
    font-size: 29px; line-height: 47px;
    color: var(--text-green);
    white-space: nowrap;
  }
  .services__list li::before { content: "•"; margin-right: 3px; }
  .trainer-photo { position: absolute; left: 780px; top: 0; width: 420px; height: 380px; }
  .divider {
    position: absolute; left: 0; top: 386px; width: 1200px; height: 10px;
    background: var(--band-line);
  }
  .testimonial__title {
    position: absolute; left: 74px; top: 404px;
    font-size: 27px; line-height: 32px; letter-spacing: 1px;
    color: var(--brand-green); font-weight: 400;
  }
  .testimonial__quote {
    position: absolute; left: 52px; top: 445px; width: 752px;
    font-size: 19px; line-height: 26.5px; text-align: center;
    color: var(--text-green); white-space: nowrap;
  }
  .testimonial__author {
    position: absolute; left: 600px; top: 527px; width: 252px;
    text-align: right; font-size: 19px; line-height: 24px; color: var(--text-green);
  }
  .trainer-name {
    position: absolute; left: 850px; top: 437px; width: 330px; text-align: center;
    font-family: "Tinos", "Times New Roman", serif; color: var(--brand-green);
    white-space: nowrap;
  }
  .trainer-name__name { font-style: italic; font-weight: 700; font-size: 34px; line-height: 44px; }
  .trainer-name__role { font-weight: 700; font-size: 29px; line-height: 40px; transform: scaleX(0.82); }
  .qual-line {
    position: absolute; left: 0; top: 559px; width: 1200px; height: 5px;
    background: var(--band-line);
  }
  .qualifications {
    position: absolute; left: 0; top: 569px; width: 1200px; height: 194px;
    background: var(--pale-green); text-align: center; color: var(--text-green);
  }
  .qualifications__title {
    font-size: 41px; font-weight: 400; line-height: 48px; padding-top: 3px;
    color: var(--brand-green);
  }
  .qualifications__list { list-style: none; font-size: 23px; line-height: 32.7px; white-space: nowrap; }
  .brand {
    position: absolute; left: 0; top: 768px; width: 1200px; height: 68px;
    display: flex; align-items: center; justify-content: center; gap: 12px;
  }
  .brand__mark { width: 30px; height: 30px; background: var(--brand-green); }
  .brand__name { font-weight: 700; font-size: 36px; color: var(--brand-green); }
</style>
</head>
<body>
<main class="profile">
  <section class="services">
    <h2 class="services__title">How I can help you?</h2>
    <ul class="services__list">
      <li>Reduce body fat&nbsp; and increase body definition</li>
      <li>Increase stamina, improve agility and speed</li>
      <li>Increase strength and size</li>
      <li>Plyometric training and conditioning</li>
      <li>Flexibility and core strength</li>
    </ul>
    <svg class="trainer-photo" viewBox="0 0 420 380" role="img" aria-label="Portrait photo of the personal trainer smiling, wearing a green polo shirt">
      <defs>
        <linearGradient id="photoTone" x1="0" y1="0" x2="0" y2="1">
          <stop offset="0" stop-color="#d7e6a6"/>
          <stop offset="1" stop-color="#b9d27a"/>
        </linearGradient>
      </defs>
      <polygon points="50,0 6,258 60,380 420,380 420,0" fill="url(#photoTone)" stroke="#ffffff" stroke-width="6"/>
    </svg>
  </section>
  <div class="divider"></div>
  <h3 class="testimonial__title">What my clients say about me?</h3>
  <p class="testimonial__quote">"With Daniel my training is always challenging and fun. I don’t remember a<br>session to be boring or repetitive. In short time I improved my core strength<br>and flexibility. I can run 10k without stopping. It is amazing improvement.&nbsp; "</p>
  <p class="testimonial__author">Sarah Whitlow</p>
  <div class="trainer-name">
    <div class="trainer-name__name">DANIEL OKAFOR</div>
    <div class="trainer-name__role">- personal trainer -</div>
  </div>
  <div class="qual-line"></div>
  <section class="qualifications">
    <h3 class="qualifications__title">Qualifications</h3>
    <ul class="qualifications__list">
      <li>Advanced Circuit Training</li>
      <li>Advanced Diploma in Personal Training - Level 3 CFPR Registered</li>
      <li>Fitness Instructor - Level 2 CFPR Registered</li>
      <li>Also qualified in – Suspension training, Studio Cycling, Sports Nutrition, Weight Management</li>
    </ul>
  </section>
  <footer class="brand">
    <span class="brand__mark"></span>
    <span class="brand__name">Brackmoor Wellness</span>
  </footer>
</main>
</body>
</html>
```